Wendrows Accountants and Tax Agents Practice

We need an update on our logo.
We require Letterhead, withcomp slips, and business cards for three partners
We currently have a logo and which is used on our letterheads but we need a much more professional and updated more modern version.
We are an Accounting Practice which needs upating. I will up load what we currently use and please use the all the wording and what another designer has proposed but need it to be different .
The colour scheme needs to be deep charcoal and a deep blue/green(065A7F) .

Target Market(s)

Individuals, companies, partnerships

Industry/Entity Type

Accounting

Font styles to use
Other font styles liked:
• ITC Avant Garde Gothic.

Colors
0393ce

Requirements
Must have
• Please follow the letter head upload the colour code and the colour charcoal.
• I would like the word Wendrows in bold Accountants (not bold) the font to be ITC Avant Garde Gothic.
• The business cards for all three partners need to have two sides the solid colour on one side with the name Wendrows Accountants. The other side with the name and details ( below details for each partner) Dorian Fellbracke FCPA, Gerald Trumbleton FCPA
• Martin Osgood (Blue/green) the T, F, E, W ( blue green) the rest in charcoal with white background
• FCPA
• 2718 Park Road Malvern VIC 3144
• T +61 3 94827713
• F + 61 9482 7159
• E martin@wendrows-example.com.au
• W wendrowsaccountants-example.com.au
• the letter faded letter G on the white side of the card in the top RH corner
Nice to have
• the letter G on the white side of the business card in shades of charcoal very faint
• Instead of E: for email using symbols for the details eg:✉

```html
<!DOCTYPE html>
<html lang="en">
<head>
<meta charset="utf-8">
<title>Wendrows Accountants – Stationery</title>
<link href="https://fonts.googleapis.com/css2?family=Arimo:wght@400;700&family=Questrial&display=swap" rel="stylesheet">
<style>
:root{
  --charcoal:#2b2a28;
  --ink:#222;
  --blue:#3f8fd2;
  --paper:#ffffff;
  --backdrop:#c4c4c4;
  --faint:#f3f3f3;
  --badge-blue:#2f5da8;
  --badge-yellow:#f2d23a;
  --sig:#cfe2f4;
}
*{box-sizing:border-box;margin:0;padding:0}
html,body{width:1200px;height:1200px;overflow:hidden;background:var(--backdrop)}
body{position:relative;font-family:"Arimo",sans-serif;color:var(--ink)}

/* Wordmark: one face, one weight, one colour */
.wordmark{display:inline-block;font-family:"Questrial",sans-serif;font-weight:400;color:var(--charcoal);text-transform:uppercase;line-height:1}
.wordmark .firm{display:block}
.wordmark .practice{display:block;text-align:right}

/* Faint corner disc */
.disc{position:absolute;border-radius:50%;background:var(--faint)}

/* Letterhead */
.letterhead{position:absolute;left:172px;top:166px;width:640px;height:909px;background:var(--paper);box-shadow:0 1px 3px rgba(0,0,0,.25);overflow:hidden}
.letterhead .disc{left:380px;top:634px;width:290px;height:290px}
.letterhead .wordmark{position:absolute;left:56px;top:56px}
.letterhead .firm{font-size:34px;letter-spacing:.5px}
.letterhead .practice{font-size:10.5px;letter-spacing:3.2px;margin-top:1px;margin-right:-3px}
.contact{position:absolute;right:52px;top:43px;font-family:"Questrial",sans-serif;font-size:10.5px;line-height:16px;color:var(--ink);white-space:nowrap}
.contact li{list-style:none;display:flex;align-items:center;gap:5px}
.contact svg{width:8px;height:8px;fill:var(--blue)}
.contact .web{color:var(--blue);margin-top:3px;font-size:11px}
.recipient{position:absolute;left:74px;top:192px;font-family:"Questrial",sans-serif;font-size:11px;line-height:12px;font-style:normal}
.letter-body{position:absolute;left:74px;top:290px;width:505px;font-size:9.6px;line-height:15.2px}
.letter-body .salutation{font-size:12.5px;margin-bottom:10px}
.letter-body p{margin-bottom:15px}
.signoff{position:absolute;left:74px;top:658px;font-size:12px}
.signature{position:absolute;left:74px;top:684px;width:90px;height:45px;background:var(--sig)}
.signer{position:absolute;left:74px;top:744px;font-size:12px;line-height:15px}
.signer b{font-size:9.5px;display:block}
.badge{position:absolute;left:74px;top:828px;width:98px;height:43px;display:flex}
.badge i{flex:1.6;background:var(--badge-blue)}
.badge i+i{flex:1;background:var(--badge-yellow)}
.directors{position:absolute;left:187px;top:829px;display:flex;gap:9px;font-size:10px;line-height:13px}
.directors h4{font-weight:400;color:var(--blue);font-size:10px}

/* Business cards */
.card{position:absolute;left:850px;width:269px;height:147px;box-shadow:0 1px 3px rgba(0,0,0,.3);overflow:hidden}
.card-front{top:166px;background:var(--paper)}
.card-front .disc{left:172px;top:24px;width:100px;height:100px}
.card-front .wordmark{position:absolute;left:15px;top:15px}
.card-front .firm{font-size:18px}
.card-front .practice{font-size:5.5px;letter-spacing:1.8px;margin-right:-2px}
.card-front .name{position:absolute;left:15px;top:57px;font-family:"Questrial",sans-serif;color:var(--blue);font-size:9px;font-weight:700}
.card-details{position:absolute;left:15px;top:74px;font-family:"Questrial",sans-serif;font-size:7.2px;line-height:11.5px;color:var(--ink);white-space:nowrap}
.card-details li{list-style:none;display:flex;align-items:center;gap:4px}
.card-details svg{width:6px;height:6px;fill:var(--blue)}
.card-details .web{color:var(--blue);margin-top:3px;font-size:7.8px}
.card-front .band{position:absolute;left:0;bottom:0;width:100%;height:10px;background:var(--charcoal)}
.card-back{top:332px;background:var(--charcoal);display:flex;align-items:center;justify-content:center}
.card-back .wordmark{color:#fff}
.card-back .firm{font-size:34px}
.card-back .practice{font-size:10.5px;letter-spacing:3.2px;margin-right:-3px}
</style>
</head>
<body>

<section class="letterhead">
  <div class="disc" aria-hidden="true"></div>
  <div class="wordmark"><span class="firm">Wendrows</span><span class="practice">Accountants</span></div>

  <ul class="contact">
    <li><svg viewBox="0 0 10 10"><path d="M2 0l2 2.5-1.2 1.2a6 6 0 0 0 3.5 3.5L7.5 6 10 8 8.5 10C4 10 0 6 0 1.5z"/></svg>+61 3 94827713</li>
    <li><svg viewBox="0 0 10 10"><path d="M2.5 0h5v10h-5zM3.5 1v7.5h3V1z"/></svg>+61 3 9482 7159</li>
    <li><svg viewBox="0 0 10 10"><path d="M0 2h10v6H0z"/></svg>info@wendrowsaccountants-example.com.au</li>
    <li class="web">www.wendrowsaccountants-example.com.au</li>
  </ul>

  <address class="recipient">2718 Park Road<br>Malvern, Victoria 3144<br>Australia</address>

  <div class="letter-body">
    <p class="salutation">Dear Sir,</p>
    <p>Lorem Ipsum. Proin gravida nibh vel velit auctor aliquet. Aenean sollicitudin, lorem quis bibendum auctor, nisi elit consequat ipsum, nec sagittis sem nibh id elit. Duis sed odio sit amet nibh vulputate cursus a sit amet mauris. Morbi accumsan ipsum velit. Nam nec tellus a odio tincidunt auctor a ornare odio. Sed non mauris vitae erat consequat auctor eu in elit.</p>
    <p>Class aptent taciti sociosqu ad litora torquent per conubia nostra, per inceptos himenaeos. Mauris in erat justo. Nullam ac urna eu felis dapibus condimentum sit amet a augue. Sed non neque elit. Sed ut imperdiet nisi. Proin condimentum fermentum nunc. Etiam pharetra, erat sed fermentum feugiat, velit mauris egestas quam, ut aliquam massa nisl quis neque. Suspendisse in orci enim.</p>
    <p>Lorem Ipsum. Proin gravida nibh vel velit auctor aliquet. Aenean sollicitudin, lorem quis bibendum auctor, nisi elit consequat ipsum, nec sagittis sem nibh id elit. Duis sed odio sit amet nibh vulputate cursus a sit amet mauris. Morbi accumsan ipsum velit. Nam nec tellus a odio tincidunt auctor a ornare odio. Sed non mauris vitae erat consequat auctor eu in elit. fermentum feugiat, velit mauris egestas quam, ut aliquam massa nisl .</p>
    <p>Class aptent taciti sociosqu ad litora torquent per conubia nostra, per inceptos himenaeos. Mauris in erat justo. Nullam ac urna eu felis dapibus condimentum sit amet a augue. Sed non neque elit. Sed ut imperdiet nisi. Proin condimentum fermentum nunc. Etiam pharetra, erat sed fermentum feugiat, velit mauris egestas quam, ut aliquam massa nisl quis neque. Suspendisse in orci enim.</p>
  </div>

  <p class="signoff">Kind Regards,</p>
  <div class="signature" role="img" aria-label="Handwritten signature of Martin Osgood in blue ink"></div>
  <div class="signer"><b>Martin Osgood, FCPA</b>Owner and Principal</div>

  <div class="badge" role="img" aria-label="Professional body membership badge"><i></i><i></i></div>
  <div class="directors">
    <h4>Directors</h4>
    <div>Gerald Trumbleton, FCPA<br>Dorian Fellbracke, FCPA<br>Martin Osgood, FCPA</div>
  </div>
</section>

<section class="card card-front">
  <div class="disc" aria-hidden="true"></div>
  <div class="wordmark"><span class="firm">Wendrows</span><span class="practice">Accountants</span></div>
  <p class="name">Martin Osgood, FCPA</p>
  <ul class="card-details">
    <li><svg viewBox="0 0 10 10"><path d="M5 0a3.5 3.5 0 0 1 3.5 3.5C8.5 6 5 10 5 10S1.5 6 1.5 3.5A3.5 3.5 0 0 1 5 0zm0 2a1.5 1.5 0 1 0 0 3 1.5 1.5 0 0 0 0-3z"/></svg>2718 Park Road Malvern Vic.3144</li>
    <li><svg viewBox="0 0 10 10"><path d="M2 0l2 2.5-1.2 1.2a6 6 0 0 0 3.5 3.5L7.5 6 10 8 8.5 10C4 10 0 6 0 1.5z"/></svg>+61 3 9482 7713</li>
    <li><svg viewBox="0 0 10 10"><path d="M2 0h5v3H2zM0 4h10v4H8v2H2V8H0z"/></svg>+61 3 9482 7159</li>
    <li><svg viewBox="0 0 10 10"><path d="M0 2h10v6H0z"/></svg>martin@wendrowsaccountants-example.com.au</li>
    <li class="web">www.wendrowsaccountants-example.com.au</li>
  </ul>
  <div class="band"></div>
</section>

<section class="card card-back">
  <div class="wordmark"><span class="firm">Wendrows</span><span class="practice">Accountants</span></div>
</section>

</body>
</html>
```